Hip, Modern Home Page for Successful SEO Expert

Marcus Delwyn is an SEO expert, author and professional speaker. His site is
www.marcusdelwyn.net. We need a re-design of the website so that it does not look outdated or like an off-the-shelf Wordpress template (like it currently does). The new design must convey to the visitor a compelling call-to-action. Specially, this home page will act as a “squeeze page” and thus, the primary marketing goal will be to get the user to opt in to our list. The new design will provide elements of “social proof” such as written testimonials, a portfolio of case studies, client logos, “as appeared on” logos, client testimonial video, etc.
Updates

Please incorporate the recently uploaded headshots into your design 

Target Market(s)

People looking for help in internet marketing for their websites, entrepreneurs, start-ups, bloggers, companies looking to build an online presence, conferences looking to book Marcus for speaking. Small business people and SEO newbies interested in buying Marcus’s video-based training (RankCraftLab.net).

Industry/Entity Type

Marketing

Font styles to use
Sans Serif

Colors
f68d4d
3276b5
8769ae
acd036

Requirements
Must have
• strong call to action
Should not have
• should not look like a template. should not use old style fonts. should not have more than one page scroll

```html
<!DOCTYPE html>
<html lang="en">
<head>
<meta charset="utf-8">
<title>Marcus Delwyn — SEO Expert, Author, Professional Speaker</title>
<link href="https://fonts.googleapis.com/css2?family=Open+Sans:wght@400;600;700;800&display=swap" rel="stylesheet">
<style>
:root{
  --orange:#e07a2c;
  --orange-dark:#b85a17;
  --orange-light:#f68d4d;
  --blue:#3276b5;
  --purple:#8769ae;
  --green:#8fb62e;
  --ink:#333;
  --muted:#777;
  --line:#e2e2e2;
  --dark:#2f2f2f;
}
*{box-sizing:border-box;margin:0;padding:0}
html,body{width:831px;height:1200px;overflow:hidden}
body{font-family:'Open Sans',Arial,sans-serif;color:var(--ink);background:#fff;font-size:10px;line-height:1.45}
.wrap{width:690px;margin:0 auto;position:relative}

/* header + hero */
.site-header{height:268px;background:linear-gradient(180deg,var(--orange-light) 0%,var(--orange) 45%,var(--orange-dark) 100%);color:#fff}
.topbar{display:flex;align-items:flex-start;justify-content:space-between;padding-top:14px}
.brand-name{font-size:17px;font-weight:700;letter-spacing:.5px;line-height:1.1}
.brand-tag{font-size:8px;opacity:.9}
.main-nav{display:flex;gap:16px;font-size:9.5px;font-weight:600;margin-top:8px;margin-left:150px}
.social{display:flex;gap:6px;margin-top:4px}
.social span{width:14px;height:14px;border-radius:50%;background:#fff;opacity:.9}
.hero{display:flex;justify-content:space-between;margin-top:26px}
.hero-copy{width:255px;padding-top:22px}
.hero-title{font-size:19px;font-weight:800;line-height:1.15;text-transform:uppercase}
.hero-text{font-size:8px;margin-top:8px;opacity:.85}
.dots{display:flex;gap:4px;margin-top:14px}
.dots i{width:7px;height:7px;border-radius:50%;background:#fff;opacity:.6}
.dots i:first-child{opacity:1}
.hero-video{width:300px;height:168px;border:4px solid #fff;border-radius:3px;position:relative;background:linear-gradient(135deg,#4a6a8c,#8b7560 55%,#3c3c3c);box-shadow:0 4px 10px rgba(0,0,0,.3)}
.play{position:absolute;left:50%;top:50%;width:34px;height:34px;margin:-17px 0 0 -17px;border-radius:50%;background:rgba(0,0,0,.55);border:2px solid #fff}
.play svg{position:absolute;left:11px;top:8px}

/* intro */
.intro{display:flex;justify-content:space-between;padding-top:26px;height:205px}
.intro-bio{width:410px}
.section-title{font-size:17px;font-weight:600;color:#444}
.intro-bio p{font-size:8px;color:var(--muted);margin-top:6px}
.optin{width:220px}
.optin-title{font-size:13px;font-weight:700;color:var(--orange);line-height:1.2}
.optin-sub{font-size:9.5px;color:var(--orange);font-weight:600}
.optin p{font-size:7.5px;color:var(--muted);margin-top:6px}
.optin-field{margin-top:8px;height:20px;border:1px solid #ccc;border-radius:2px;font-size:7.5px;color:#999;padding:4px 6px}
.optin-btn{margin-top:6px;display:inline-block;background:var(--dark);color:#fff;font-size:8px;font-weight:700;padding:5px 12px;letter-spacing:.5px}

/* portfolio */
.portfolio{display:flex;justify-content:space-between;height:245px}
.block-title{font-size:14px;font-weight:700;color:var(--green);text-transform:uppercase;display:flex;align-items:center;gap:10px;margin-bottom:10px}
.block-title::after{content:"";flex:1;height:1px;background:var(--line)}
.thumbs{display:grid;grid-template-columns:repeat(5,88px);gap:8px;width:472px}
.thumb{height:60px;border:1px solid #ddd}
.t1{background:#3d6b8e}.t2{background:#7fae3a}.t3{background:#c9d9e6}.t4{background:#2e7f5a}.t5{background:#a3c64a}
.t6{background:#5b8fc2}.t7{background:#e0e6d8}.t8{background:#3a3a3a}.t9{background:#6d9a35}.t10{background:#d8c6a4}
.t11{background:#b6c9db}.t12{background:#8769ae}.t13{background:#4c8bb8}.t14{background:#c7d58c}.t15{background:#e7e2d4}
.testimonials{width:200px;height:222px;background:var(--dark);color:#ddd;padding:14px 16px;margin-top:4px}
.testimonials-head{display:flex;justify-content:space-between;align-items:center;color:#fff;font-size:15px}
.testimonials-head span{font-size:10px;letter-spacing:3px}
.quote{font-size:20px;color:#777;line-height:1;margin-top:10px;font-weight:700}
.testimonials p{font-size:7.5px;margin-top:2px;color:#bbb}
.testimonials .author{margin-top:10px;font-size:8px;color:#fff}

/* logos */
.logo-row{display:flex;align-items:center;height:58px;border-top:1px solid var(--line)}
.logo-row .label{font-size:13px;color:var(--muted);width:100px;flex:none}
.logo-row .label b{color:var(--blue);font-weight:600}
.logos{display:flex;flex:1;justify-content:space-between;align-items:center}
.logo{font-size:9px;font-weight:700;color:#666;display:flex;align-items:center;gap:4px}
.logo i{width:8px;height:8px;background:#999;display:inline-block}

/* blog */
.blog{padding-top:22px;border-top:1px solid var(--line)}
.blog .block-title{color:#444}
.posts{display:flex;justify-content:space-between}
.post{width:215px;display:flex;gap:8px}
.post-thumb{width:54px;height:44px;flex:none}
.post h4{font-size:9px;font-weight:600;color:#444}
.post p{font-size:7.5px;color:var(--muted)}

/* footer */
.site-footer{position:absolute;left:0;top:1112px;width:831px;height:88px;background:linear-gradient(180deg,var(--orange),var(--orange-dark));color:#fff;text-align:center;padding-top:26px}
.footer-nav{display:flex;justify-content:center;gap:22px;font-size:8.5px;font-weight:600}
.copyright{font-size:7px;opacity:.8;margin-top:10px}
</style>
</head>
<body>
<header class="site-header">
  <div class="wrap">
    <div class="topbar">
      <div class="brand">
        <div class="brand-name">MARCUS DELWYN</div>
        <div class="brand-tag">SEO expert, author, professional speaker</div>
      </div>
      <nav class="main-nav"><span>Home</span><span>Article</span><span>Books</span><span>Speaking</span><span>Blog</span><span>Testimonial</span><span>Portfolio</span></nav>
      <div class="social"><span></span><span></span></div>
    </div>
    <section class="hero">
      <div class="hero-copy">
        <h1 class="hero-title">Phasellus scelerisque morbi diam mauris</h1>
        <p class="hero-text">Lorem ipsum dolor sit amet consectetur adipiscing elit. Sed posuere sem eu metus volutpat, vitae ultrices nibh dictum. Donec vel lorem non neque faucibus tempor.</p>
        <div class="dots"><i></i><i></i><i></i><i></i></div>
      </div>
      <div class="hero-video" role="img" aria-label="Video still of Marcus Delwyn being interviewed in a studio">
        <div class="play"><svg width="14" height="16" viewBox="0 0 14 16"><path d="M0 0L14 8L0 16Z" fill="#fff"/></svg></div>
      </div>
    </section>
  </div>
</header>

<main class="wrap">
  <section class="intro">
    <div class="intro-bio">
      <h2 class="section-title">Who is Marcus</h2>
      <p>Marcus Delwyn is co-author of The Craft of Search and author of Search Power Playbook, both published by Northgate Press. He founded the agency Linkwell Studio in the 1990s and grew it into a respected search firm before its sale.</p>
      <p>Marcus has worked with brands large and small, helping them earn lasting visibility in search. He speaks at marketing events around the world and teaches practical methods through his video courses at RankCraftLab.net. Clients praise his clear, hands-on approach to growth.</p>
    </div>
    <aside class="optin">
      <div class="optin-title">Learn How to Make $10,000</div>
      <div class="optin-sub">Per Month Blogging 2 Hours a Day</div>
      <p>Enter your email to join my newsletter and download the blog post ideas guide instantly.</p>
      <div class="optin-field">Email address</div>
      <div class="optin-btn">SUBSCRIBE</div>
    </aside>
  </section>

  <section class="portfolio">
    <div>
      <h2 class="block-title">Recent Portfolio</h2>
      <div class="thumbs">
        <div class="thumb t1" role="img" aria-label="Website screenshot"></div>
        <div class="thumb t2" role="img" aria-label="Website screenshot"></div>
        <div class="thumb t3" role="img" aria-label="Website screenshot"></div>
        <div class="thumb t4" role="img" aria-label="Website screenshot"></div>
        <div class="thumb t5" role="img" aria-label="Website screenshot"></div>
        <div class="thumb t6" role="img" aria-label="Website screenshot"></div>
        <div class="thumb t7" role="img" aria-label="Website screenshot"></div>
        <div class="thumb t8" role="img" aria-label="Website screenshot"></div>
        <div class="thumb t9" role="img" aria-label="Website screenshot"></div>
        <div class="thumb t10" role="img" aria-label="Website screenshot"></div>
        <div class="thumb t11" role="img" aria-label="Website screenshot"></div>
        <div class="thumb t12" role="img" aria-label="Website screenshot"></div>
        <div class="thumb t13" role="img" aria-label="Website screenshot"></div>
        <div class="thumb t14" role="img" aria-label="Website screenshot"></div>
        <div class="thumb t15" role="img" aria-label="Website screenshot"></div>
      </div>
    </div>
    <aside class="testimonials">
      <div class="testimonials-head">Testimonials <span>‹ ›</span></div>
      <div class="quote">“</div>
      <p>Working with Marcus changed how we think about search. Our traffic doubled within months and the team finally understands what drives real results. His advice is clear, honest and practical, and we keep coming back for more.</p>
      <div class="author">– By Author Name</div>
    </aside>
  </section>

  <section class="logo-row">
    <div class="label">Our <b>Clients</b></div>
    <div class="logos">
      <span class="logo">Brightmoor</span><span class="logo"><i></i>Tallow</span><span class="logo">Verano</span><span class="logo">Pixelhaus</span><span class="logo">Oakridge</span><span class="logo"><i></i>Fernly</span><span class="logo">Corvant</span><span class="logo">Lumio</span>
    </div>
  </section>
  <section class="logo-row">
    <div class="label">as <b>appeared on</b></div>
    <div class="logos">
      <span class="logo">Quietwave</span><span class="logo"><i></i>Daily Ledger</span><span class="logo">Netrail</span><span class="logo">Bizwire</span><span class="logo">Techpost</span><span class="logo"><i></i>Cinder</span><span class="logo">Marketline</span>
    </div>
  </section>

  <section class="blog">
    <h2 class="block-title">Blog Post</h2>
    <div class="posts">
      <article class="post"><div class="post-thumb" style="background:#9a8f86" role="img" aria-label="Blog post photo"></div><div><h4>Aliquam nec erat</h4><p>Pellentesque nec ultrices dui, sed tempus neque. Donec semper massa vitae lorem.</p></div></article>
      <article class="post"><div class="post-thumb" style="background:#6f8fae" role="img" aria-label="Blog post photo"></div><div><h4>Maecenas at justo</h4><p>Curabitur vitae lacus at nibh porta varius. Nulla facilisi, morbi ut tellus.</p></div></article>
      <article class="post"><div class="post-thumb" style="background:#c79a6a" role="img" aria-label="Blog post photo"></div><div><h4>Phasellus felis dolor</h4><p>Integer vel mauris quis lorem gravida tempor. Fusce id risus eget magna.</p></div></article>
    </div>
  </section>
</main>

<footer class="site-footer">
  <nav class="footer-nav"><span>HOME</span><span>BIOGRAPHY</span><span>ARTICLES</span><span>PORTFOLIO</span><span>TESTIMONIALS</span><span>VIDEO</span><span>BLOG</span><span>NEWS</span><span>CONTACT</span></nav>
  <div class="copyright">© 2014 Marcus Delwyn. All rights reserved. www.marcusdelwyn.net</div>
</footer>
</body>
</html>
```